Web-Design  für naturwissenschaflich-philosophische Institution
Zielgruppe
Es handelt sich um eine naturwissenschaflich-philosophische Institution. Besucher sind neben Natur- und Geisteswissenschaftlern auch interessierte Laien.
Kernthema der Seite ist alles rund um das Thema Zahlen, allerdings unter einem naturwissenschaftlich, philosophischen Aspekt. Nach einer grundsätzlichen Erklärung (Leitartikel 'Als Flüsse singen') baut die Seite sich auf aus zahreichen Beispielen/Beiträgen aus den unterschiedlichsten Fachbereichen, die scheinbar keinerlei Bezug zueinander haben, wie Mathematik, Geometrie einerseits und der großen Literatur einschließlich historischer und religiöser Schriften andererseits. Immer aber gibt es einen Bezug zu fraktal wachsenden Dreiecken.
Die Artikel sind meist populärwissenschaftlich formuliert. Es handelt sich nicht um esoterische Inhalte, auch wenn der Domainname www.kelmbrauth.de das evtl. vermuten ließe. Keine Berührung zu Spiritualität. Die Institution ist im Aufbau und hat durchaus den Anspruch, diese klassischen Themen modern aufzugreifen. Sie ist nicht verstaubt.
Aufgabenstellung
Geordneter, klarer, transparenter Aufbau. Übersichtlich und strukturiert, wie zB www.qrl.de Es sollten geometrische Proportionen eingehalten werden (wie Symmetrie, goldener Schnitt). Nicht zu viele verschiedene Stilelemente. Die Seite sollte einladend sein, ggf. ansprechendes Bild auf Startseite (mit Bezug zu Zahlen, Geoemetrie).
Die Startseite braucht nun im Header kein Logo mehr zu haben. Der Seitentitel sollte sein 'Das Echo der Wolken'. Siehe Anhang 'Header Beispiel'
Als Menüpunkte benötigen wir neben Home, nur 'Beiträge', 'Buch', 'Kontakt' oder einfach nur die bekannten drei Striche. Der Link zum Impressum genügt im Footer. Rechts oben benötigt man ein Suchfeld.
Besonderheit: Man benötigt eine Art zweiten Header, der aus einer Zahlenreihe besteht. Die einzelnen Zahlen müssen später verlinkt sein auf Unterseiten. Siehe Muster im Anhang. Der User muss sie als Link erkennen können (evtl. Programmierthema: zB Hervorheben beim drüberhoovern). Die Zahlen müssen erweiterbar sein, ggf. über Pfeil klicken, siehe
Es gibt einen zentralen Startartikel. Auf diesen muss man leicht kommen. Im Muster heißt er 'Als die Flüsse singen'.
Das Bild hier ist sehr wichtig. Es sollte bestehn aus vielen interessanten Zahlen, wie in 'Zahlenwolke' angegeben. Und möglichst auch den Dreiecken wie in 'Logo1'.
Weiter unten auf der Startseite sollte es dann weitere Elemente geben, einmal wo man zu bestimmten Unterkategorien kommt, im Muster sind das 'Bibel und Zahlen' 'Naturwissenschaft' etc. und dann evtl weiter unten noch ein Stilelemente, in welchem man die neuesten Artikel verlinken kann.

```html
<!DOCTYPE html>
<html lang="de">
<head>
<meta charset="utf-8">
<title>Das Echo der Wolken</title>
<link href="https://fonts.googleapis.com/css2?family=Poppins:wght@400;500;600;700&display=swap" rel="stylesheet">
<style>
  :root {
    --blue: #1287fd;
    --ink: #22344a;
    --band: #ededed;
    --card: #f1f1f1;
    --white: #ffffff;
  }
  * { margin: 0; padding: 0; box-sizing: border-box; }
  html, body { width: 1152px; height: 1200px; overflow: hidden; }
  body { font-family: "Poppins", sans-serif; color: var(--ink); background: var(--white); position: relative; }

  .site-header { position: absolute; left: 0; top: 0; width: 1152px; height: 60px; background: var(--white); box-shadow: 0 1px 3px rgba(0,0,0,.08); z-index: 2; }
  .site-title { position: absolute; left: 168px; top: 16px; font-size: 21px; color: var(--blue); font-weight: 400; letter-spacing: .2px; }
  .site-title strong { font-weight: 600; }
  .main-nav { position: absolute; left: 520px; top: 23px; display: flex; align-items: center; font-size: 10.5px; font-weight: 600; }
  .main-nav a { color: var(--ink); text-decoration: none; }
  .main-nav .sep { width: 1px; height: 9px; background: #c8ccd2; margin: 0 12px; }
  .main-nav a.active { color: var(--blue); position: relative; }
  .main-nav a.active::after { content: ""; position: absolute; left: 0; right: 0; bottom: -6px; height: 2px; background: var(--blue); }
  .search { position: absolute; left: 864px; top: 18px; width: 120px; height: 24px; border: 1px solid #8c939c; border-radius: 2px; }
  .search span { position: absolute; left: 6px; top: 5px; font-size: 10px; color: #d3d6da; }
  .search svg { position: absolute; right: 6px; top: 5px; }

  .number-bar { position: absolute; left: 0; top: 60px; width: 1152px; height: 36px; background: var(--band); border-bottom: 1px solid #8f8f8f; }
  .number-bar .label { position: absolute; right: 437px; top: 10px; font-size: 10.5px; font-weight: 500; }
  .number-bar .arrow { position: absolute; top: 14px; width: 0; height: 0; border-top: 3.5px solid transparent; border-bottom: 3.5px solid transparent; }
  .arrow.prev { left: 740px; border-right: 5px solid var(--ink); }
  .arrow.next { left: 979px; border-left: 5px solid var(--blue); }
  .numbers { position: absolute; left: 756px; top: 9px; display: flex; gap: 6px; }
  .numbers a { width: 18px; height: 18px; border-radius: 3px; background: var(--ink); color: var(--white); font-size: 12px; font-weight: 600; text-align: center; line-height: 19px; text-decoration: none; }
  .numbers a.current { background: var(--blue); }

  .hero { position: absolute; left: 0; top: 96px; width: 1152px; height: 504px; background: var(--band); border-bottom: 1px solid #8f8f8f; overflow: hidden; }
  .hero-visual { position: absolute; left: 612px; top: 0; width: 540px; height: 504px; background: linear-gradient(160deg, #dbe8f6 0%, #9cc8f8 55%, #4fa3fb 100%); }
  .hero h1 { position: absolute; left: 168px; top: 150px; font-size: 55px; font-weight: 700; line-height: 60px; letter-spacing: -.5px; color: var(--ink); }
  .btn { display: block; background: var(--blue); color: var(--white); font-size: 11px; font-weight: 500; text-align: center; line-height: 36px; height: 36px; text-decoration: none; }
  .hero .btn { position: absolute; left: 168px; top: 305px; width: 219px; }

  .categories { position: absolute; left: 168px; top: 690px; display: flex; gap: 23px; }
  .card { width: 257px; height: 300px; background: var(--card); box-shadow: 0 1px 4px rgba(0,0,0,.12); position: relative; padding: 25px 20px 0 25px; }
  .card h2 { font-size: 28px; font-weight: 600; line-height: 33px; height: 66px; overflow-wrap: anywhere; }
  .card p { font-size: 10.5px; line-height: 15.5px; margin-top: 24px; }
  .card .btn { position: absolute; left: 25px; top: 240px; width: 134px; }

  .to-top { position: absolute; left: 1045px; top: 1091px; width: 24px; height: 24px; background: #ececec; }
  .to-top::after { content: ""; position: absolute; left: 6px; top: 7px; border-left: 6px solid transparent; border-right: 6px solid transparent; border-bottom: 10px solid var(--ink); }

  .site-footer { position: absolute; left: 0; top: 1139px; width: 1152px; height: 61px; background: #ececec; box-shadow: 0 -2px 4px rgba(0,0,0,.04); }
</style>
</head>
<body>
  <header class="site-header">
    <div class="site-title"><strong>Das Echo</strong> der Wolken</div>
    <nav class="main-nav">
      <a href="#" class="active">HOME</a><span class="sep"></span>
      <a href="#">BETRAGE</a><span class="sep"></span>
      <a href="#">BUCH</a><span class="sep"></span>
      <a href="#">KONTAKT</a><span class="sep"></span>
      <a href="#">IMPRESSUM</a>
    </nav>
    <div class="search">
      <span>Suche</span>
      <svg width="12" height="12" viewBox="0 0 12 12"><circle cx="7" cy="5" r="3.8" fill="none" stroke="#22344a" stroke-width="1.2"/><line x1="4.3" y1="7.7" x2="1" y2="11" stroke="#22344a" stroke-width="1.3"/></svg>
    </div>
  </header>

  <div class="number-bar">
    <span class="label">und was sie erzählen:</span>
    <span class="arrow prev"></span>
    <nav class="numbers">
      <a href="#" class="current">1</a><a href="#">2</a><a href="#">3</a><a href="#">4</a><a href="#">5</a><a href="#">6</a><a href="#">7</a><a href="#">8</a><a href="#">9</a>
    </nav>
    <span class="arrow next"></span>
  </div>

  <section class="hero">
    <div class="hero-visual" role="img" aria-label="Großes Dreieck aus verschachtelten blauen Dreiecken mit Zahlen und römischen Ziffern"></div>
    <h1>Als die<br>Flüsse singen ...</h1>
    <a href="#" class="btn">Lern mehr</a>
  </section>

  <section class="categories">
    <article class="card">
      <h2>Bibel und Zahlen</h2>
      <p>Die Heilige Schrift ist ein Werk aus Zahlen. Ihre Verfasser haben die archetypischen Inhalte in wundersamer Art und Weise in der Bibel. Und so weiter und so fort</p>
      <a href="#" class="btn">Lern mehr</a>
    </article>
    <article class="card">
      <h2>Naturwissenschaft</h2>
      <p>Die Heilige Schrift ist ein Werk aus Zahlen. Ihre Verfasser haben die archetypischen Inhalte in wundersamer Art</p>
      <a href="#" class="btn">Lern mehr</a>
    </article>
    <article class="card">
      <h2>Philosophie</h2>
      <p>Die Heilige Schrift ist ein Werk aus Zahlen. Ihre Verfasser haben die archetypischen Inhalte in wundersamer Art und Weise der Bibel. Und so weiter und so fort und vieles mehr das sehr schön eindrucksvoll ist</p>
      <a href="#" class="btn">Lern mehr</a>
    </article>
  </section>

  <a href="#" class="to-top" aria-label="Nach oben"></a>
  <footer class="site-footer"></footer>
</body>
</html>
```